Wine Label Marabel Faye Rose or Pinot Noir

Need label design for "Marabel Faye" wine brand.
Rose or Pinot Noir.
Thinking something pretty, floral, southern inspired.

Target Market(s)

Female- age 45-65

Font styles to use
Script

Colors
eea4c8
d2a4cc
f68e4d
fee18a

```html
<!DOCTYPE html>
<html lang="en">
<head>
<meta charset="utf-8">
<title>Marabel Faye Pinot Noir Labels</title>
<link rel="stylesheet" href="https://fonts.googleapis.com/css2?family=Allison&family=Pacifico&family=Montserrat:wght@800&family=Work+Sans:wght@400&display=swap">
<style>
  :root {
    --page: #ffffff;
    --label-pink: #efa9d7;
    --label-pink-deep: #ec94ca;
    --petal-white: #fbe9f1;
    --petal-blush: #f7cfe2;
    --petal-pink: #f0a9cd;
    --petal-magenta: #dd6fa8;
    --stem-shadow: #a86a7c;
    --rose-soft: #f4b4dc;
    --rose-mid: #ee9fd0;
    --rose-core: #e584bf;
    --gold: #fee18a;
    --white: #ffffff;
  }
  * { margin: 0; padding: 0; box-sizing: border-box; }
  html, body {
    width: 1200px;
    height: 836px;
    overflow: hidden;
    background: var(--page);
  }
  .sheet {
    position: relative;
    width: 1200px;
    height: 836px;
  }
  .label {
    position: absolute;
    top: 42px;
    width: 542px;
    height: 751px;
    overflow: hidden;
    background: linear-gradient(to bottom, var(--label-pink) 0%, var(--label-pink) 55%, var(--label-pink-deep) 100%);
  }
  .label--script { left: 41px; }
  .label--bold { left: 614px; }

  .bloom-field {
    position: absolute;
    left: 0; top: 0;
    width: 100%;
    height: 320px;
    background:
      radial-gradient(circle 70px at 15% 42%, var(--petal-white), transparent 72%),
      radial-gradient(circle 75px at 38% 28%, var(--petal-blush), transparent 72%),
      radial-gradient(circle 55px at 58% 22%, var(--petal-magenta), transparent 75%),
      radial-gradient(circle 80px at 80% 30%, var(--petal-white), transparent 72%),
      radial-gradient(circle 60px at 50% 48%, var(--petal-blush), transparent 72%),
      radial-gradient(circle 55px at 30% 55%, var(--petal-magenta), transparent 78%),
      radial-gradient(circle 70px at 72% 62%, var(--petal-blush), transparent 72%),
      radial-gradient(circle 65px at 20% 78%, var(--petal-blush), transparent 75%),
      radial-gradient(circle 60px at 92% 68%, var(--petal-pink), transparent 75%),
      linear-gradient(to bottom, var(--stem-shadow) 0%, var(--petal-pink) 12%, var(--petal-blush) 40%, var(--petal-blush) 70%, var(--label-pink) 100%);
  }
  .rose-bloom {
    position: absolute;
    left: 40px; top: 470px;
    width: 500px;
    height: 290px;
    background:
      radial-gradient(ellipse 14% 18% at 50% 48%, var(--rose-core), transparent 80%),
      radial-gradient(ellipse 28% 30% at 50% 50%, var(--rose-mid), transparent 80%),
      radial-gradient(ellipse 46% 52% at 50% 58%, var(--rose-soft), transparent 85%);
  }

  .brand-name {
    position: absolute;
    left: 0; width: 100%;
    text-align: center;
    color: var(--white);
    white-space: nowrap;
    font-weight: 400;
    transform: rotate(-6deg);
  }
  .label--script .brand-name {
    font-family: "Allison", cursive;
    font-size: 110px;
    line-height: 1;
    top: 335px;
  }
  .label--bold .brand-name {
    font-family: "Pacifico", cursive;
    font-size: 62px;
    line-height: 1.2;
    top: 340px;
  }
  .varietal {
    position: absolute;
    left: 184px;
    top: 601px;
    font-family: "Montserrat", sans-serif;
    font-weight: 800;
    font-size: 28px;
    letter-spacing: 0.5px;
    color: var(--gold);
    white-space: nowrap;
  }
  .vintage {
    position: absolute;
    left: 275px;
    top: 662px;
    font-family: "Work Sans", sans-serif;
    font-weight: 400;
    font-size: 19px;
    letter-spacing: 1.6px;
    color: var(--white);
    white-space: nowrap;
  }
</style>
</head>
<body>
<main class="sheet">
  <section class="label label--script">
    <div class="bloom-field" role="img" aria-label="Photograph of pink and white peonies"></div>
    <div class="rose-bloom" role="img" aria-label="Soft-focus photograph of a pink rose"></div>
    <h1 class="brand-name">Marabel Faye</h1>
    <p class="varietal">PINOT NOIR</p>
    <p class="vintage">CALIFORNIA, 2018</p>
  </section>
  <section class="label label--bold">
    <div class="bloom-field" role="img" aria-label="Photograph of pink and white peonies"></div>
    <div class="rose-bloom" role="img" aria-label="Soft-focus photograph of a pink rose"></div>
    <h1 class="brand-name">Marabel Faye</h1>
    <p class="varietal">PINOT NOIR</p>
    <p class="vintage">CALIFORNIA, 2018</p>
  </section>
</main>
</body>
</html>
```